Elegant sophisticated Invitation Design in A5

"Amber Hours of Vellmoor"
We are after an invitation A5 portrait size. It is for an outdoor event for a 4 course dinner. It needs to display high class, elegance and sophistication. We like the idea of having stars or reflections on the water (as per attached images we found on findora)

Text and logo are attached. The file needs to be supplied to use as psd file and needs to be 300dpi at least as the invitation will be printed.

We would like dark colours, black, and sparkles/stars.

The main focus is elegance!

Logos and text are attached.

Target Market(s)

Upper class, business men and women, Suit and tie event

Industry/Entity Type

Event

Font styles to use
Decorative
Script

Colors
fffefe
000000

Requirements
Must have
• The element of Water and stars or sparkles. It needs to speak elegance throughout. The fonts chosen need to be soft and elegant. The logo attached must be used either with the diamond or the standard version a mono version can also be used. Open for designers ideas.
Should not have
• Bold and bulky fonts it needs to be soft

```html
<!DOCTYPE html>
<html lang="en">
<head>
<meta charset="utf-8">
<title>Amber Hours of Vellmoor – VIP Dinner Invitation</title>
<link href="https://fonts.googleapis.com/css2?family=Pinyon+Script&family=Fira+Sans:wght@500;700&family=Roboto+Condensed:wght@400&display=swap" rel="stylesheet">
<style>
  :root{
    --backdrop:#b3b3b3;
    --night-deep:#03080f;
    --night-navy:#0a1d33;
    --horizon:#1c4d7a;
    --moonglow:#c9dcf0;
    --ink-white:#fffefe;
    --accent-gold:#f2b81e;
  }
  *{margin:0;padding:0;box-sizing:border-box}
  html,body{width:1200px;height:1200px;overflow:hidden;background:var(--backdrop)}
  .invitation{
    position:absolute;left:176px;top:0;width:848px;height:1200px;
    overflow:hidden;color:var(--ink-white);text-align:center;
  }
  .night-water{
    position:absolute;inset:0;
    background:
      radial-gradient(ellipse 38% 30% at 50% 52%, rgba(201,220,240,.55), rgba(201,220,240,0) 70%),
      radial-gradient(ellipse 70% 6% at 50% 14%, rgba(60,120,180,.45), rgba(28,77,122,0) 80%),
      linear-gradient(180deg,var(--night-deep) 0%,var(--night-navy) 10%,var(--horizon) 14%,var(--night-navy) 22%,#0d2744 50%,#06121f 80%,var(--night-deep) 100%);
  }
  .line{position:absolute;left:0;right:0}
  .host-name{
    top:178px;font-family:'Fira Sans',sans-serif;font-weight:500;font-size:36px;
    display:flex;justify-content:center;align-items:center;gap:12px;
  }
  .host-name .dot{width:18px;height:18px;border-radius:50%;background:var(--accent-gold)}
  .event-title{top:338px;font-family:'Pinyon Script',cursive;font-size:66px}
  .tier{top:462px;font-family:'Fira Sans',sans-serif;font-weight:700;font-size:36px;color:var(--accent-gold)}
  .banquet{top:500px;font-family:'Fira Sans',sans-serif;font-weight:700;font-size:84px;letter-spacing:-1px}
  .details{font-family:'Fira Sans',sans-serif;font-weight:700;font-size:28px}
  .details.date{top:632px}
  .details.venue{top:672px;letter-spacing:.5px}
  .details.street{top:714px}
  .details sup{font-size:12px}
  .cause{font-family:'Pinyon Script',cursive;font-size:40px}
  .cause.first{top:842px}
  .cause.second{top:892px}
  .by-invitation{top:958px;font-family:'Pinyon Script',cursive;font-size:46px}
  .perks{font-family:'Roboto Condensed',sans-serif;font-size:21px}
  .perks::before{content:"";display:inline-block;width:8px;height:8px;border-radius:50%;background:var(--ink-white);margin-right:9px;vertical-align:middle}
  .perks.one{top:1054px}
  .perks.two{top:1088px}
  .perks.three{top:1121px}
</style>
</head>
<body>
  <main class="invitation">
    <div class="night-water" role="img" aria-label="Starry night sky over dark water with moonlight reflecting on the ripples"></div>

    <div class="line host-name"><span class="dot"></span>Kestrel Ability Trust</div>

    <h1 class="line event-title">‘Amber Hours of Vellmoor’</h1>
    <p class="line tier">VIP Dinner</p>
    <h2 class="line banquet">Le Banquet</h2>

    <p class="line details date">Saturday 17<sup>th</sup> July 2017</p>
    <p class="line details venue">HARBOURLIGHT PARK</p>
    <p class="line details street">Quayline Street, South Vellmoor</p>

    <p class="line cause first">Building accessible housing for people with disability</p>
    <p class="line cause second">in North Queensland</p>

    <p class="line by-invitation">By Invitation</p>

    <p class="line perks one">Four course dinner exclusively crafted by The Saltgrove Kitchen</p>
    <p class="line perks two">Beautiful wines and fine beers included</p>
    <p class="line perks three">Live Entertainment</p>
  </main>
</body>
</html>
```